Fun Social App Need Simple, Logo, Clean App Design, and Icon

We need a app design for a new social meet up, planning app called Brindle. The look and feel should be fun, yet clean and simple. This is an app for setting up meetings with friends and family. Our motto is Live Spontaneously. What we need:

-Logo

-App Icon

-Layout App pages as shown in attached. (Most will use the same header you come up with, with perhaps a few extras as you wish to add on each page)

-A button design that can be used throughout the app that conveys "push me" We will use this button in several places and simply change the text on it.
Updates

https://pelwarkdigest.com/blog/58213-20-striking-samples-of-sparse-phone-screen-layouts#k.7x2mqvtrelaguz We like the minimalist look.

Target Market(s)

Ages 10-39 Primarily

Industry/Entity Type

Social

Font styles to use
Sans Serif

Colors

Designer to choose colors to be used in the design.

Requirements
Must have
• Would like to focus on the S in the logo/icon. A S with arrows at both tips would be good.

```html
<!DOCTYPE html>
<html lang="en">
<head>
<meta charset="utf-8">
<title>Brindle – App Screens</title>
<link rel="stylesheet" href="https://fonts.googleapis.com/css2?family=Lato:wght@300;400&display=swap">
<style>
  :root {
    --plum: #800080;
    --plum-deep: #7a0f7e;
    --lavender: #7e6fb0;
    --mist: #e4dff0;
    --white: #ffffff;
    --accent: #4cc4d8;
    --brand: #7b2a8a;
  }
  * { box-sizing: border-box; margin: 0; padding: 0; }
  html, body { width: 1200px; height: 1200px; overflow: hidden; background: var(--white); }
  body { position: relative; font-family: "Lato", sans-serif; color: var(--white); }

  .brand-lockup {
    position: absolute; left: 0; top: 40px; width: 1200px;
    display: flex; flex-direction: column; align-items: center; gap: 22px;
  }
  .brand-dot { width: 56px; height: 56px; border-radius: 50%; background: var(--brand); }
  .brand-name { font-weight: 300; font-size: 96px; line-height: 1; color: var(--brand); letter-spacing: 2px; }

  .screen {
    position: absolute; width: 359px; height: 431px; overflow: hidden;
    background:
      radial-gradient(ellipse 60% 38% at 52% 100%, rgba(255,255,255,0.85), rgba(255,255,255,0) 100%),
      linear-gradient(90deg, var(--plum) 0%, var(--plum-deep) 18%, var(--lavender) 52%, var(--lavender) 100%);
  }
  .screen--splash {
    background:
      radial-gradient(ellipse 20% 18% at 50% 0%, rgba(255,255,255,0.95), rgba(255,255,255,0) 100%),
      radial-gradient(ellipse 18% 30% at 0% 55%, rgba(255,255,255,0.95), rgba(255,255,255,0) 100%),
      radial-gradient(ellipse 28% 60% at 100% 70%, rgba(236,232,246,0.95), rgba(236,232,246,0) 100%),
      radial-gradient(ellipse 30% 25% at 0% 100%, rgba(126,111,176,0.9), rgba(126,111,176,0) 100%),
      linear-gradient(90deg, #a0409f 0%, var(--plum) 28%, var(--plum) 58%, #c79ad0 78%, var(--lavender) 100%);
  }
  .row-1 { top: 278px; }
  .row-2 { top: 754px; }
  .col-1 { left: 12px; }
  .col-2 { left: 420px; }
  .col-3 { left: 828px; }

  .screen-brand { position: absolute; left: 6px; top: 5px; font-weight: 300; font-size: 22px; }
  .screen-user { position: absolute; right: 11px; top: 7px; font-size: 14px; }
  .screen-user--light { font-weight: 300; }

  .splash-title { position: absolute; left: 0; width: 100%; top: 140px; text-align: center; font-weight: 300; font-size: 38px; }
  .splash-motto { position: absolute; left: 0; width: 100%; top: 190px; text-align: center; font-size: 15px; }
  .splash-action { position: absolute; left: 0; width: 100%; text-align: center; font-size: 15px; }
  .splash-action--login { top: 248px; }
  .splash-action--new { top: 293px; }

  .label { position: absolute; color: var(--accent); font-size: 14px; }
  .item { position: absolute; font-size: 14px; font-weight: 300; line-height: 16.6px; }
  .list { position: absolute; list-style: none; font-size: 14px; font-weight: 300; line-height: 16.6px; }

  .dash { display: inline-block; width: 9px; height: 1px; background: var(--white); vertical-align: middle; margin: 0 4px; }
</style>
</head>
<body>

  <header class="brand-lockup">
    <div class="brand-dot"></div>
    <div class="brand-name">Brindle</div>
  </header>

  <section class="screen screen--splash row-1 col-1">
    <div class="splash-title">Brindle</div>
    <div class="splash-motto">Live Spontaneously</div>
    <div class="splash-action splash-action--login">Login</div>
    <div class="splash-action splash-action--new">New User</div>
  </section>

  <section class="screen row-1 col-2">
    <div class="screen-brand">Brindle</div>
    <div class="screen-user screen-user--light">User Name</div>
    <div class="item" style="left:12px;top:137px;font-weight:400;">Your Brindles</div>
    <div class="label" style="left:13px;top:164px;">Who</div>
    <div class="label" style="left:147px;top:164px;">What</div>
    <div class="label" style="left:263px;top:164px;">When</div>
    <div class="item" style="left:13px;top:186px;font-weight:400;">Kate</div>
    <div class="item" style="left:12px;top:208px;font-weight:400;">James</div>
    <div class="item" style="left:11px;top:230px;font-weight:400;">Mom</div>
    <div class="item" style="left:139px;top:186px;">Option A</div>
    <div class="item" style="left:139px;top:208px;">Option C</div>
    <div class="item" style="left:139px;top:230px;">Option D</div>
    <div class="item" style="left:263px;top:186px;">XX</div>
    <div class="item" style="left:263px;top:208px;">XX</div>
    <div class="item" style="left:263px;top:230px;">XX</div>
  </section>

  <section class="screen row-1 col-3">
    <div class="screen-brand">Brindle</div>
    <div class="screen-user">Sarah</div>
    <div class="label" style="left:7px;top:140px;">Who ?</div>
    <ul class="list" style="left:131px;top:162px;">
      <li><span class="dash"></span>Kate<span class="dash"></span></li>
      <li style="padding-left:14px;">Jane</li>
      <li style="padding-left:14px;">Donny</li>
      <li style="padding-left:14px;">Sergei</li>
      <li style="padding-left:14px;">Marco</li>
      <li style="padding-left:14px;">Manuel</li>
      <li style="padding-left:14px;">Miguel</li>
      <li style="padding-left:14px;">Samatha</li>
      <li style="padding-left:14px;">Jen</li>
      <li style="padding-left:14px;">Mom</li>
    </ul>
  </section>

  <section class="screen row-2 col-1">
    <div class="screen-brand">Brindle</div>
    <div class="screen-user">Sarah</div>
    <div class="label" style="left:8px;top:162px;">What ?</div>
    <ul class="list" style="left:147px;top:180px;">
      <li>Type In</li>
      <li>Option A</li>
      <li>Option B</li>
      <li>Option C</li>
      <li>Option D</li>
      <li>Option E</li>
      <li>Option F</li>
      <li>Option G</li>
      <li>Option H</li>
      <li>Option I</li>
      <li>Option J</li>
    </ul>
  </section>

  <section class="screen row-2 col-2">
    <div class="screen-brand">Brindle</div>
    <div class="screen-user">Sarah</div>
    <div class="label" style="left:8px;top:162px;">When ?</div>
    <ul class="list" style="left:23px;top:181px;">
      <li>x1</li><li>x2</li><li>x3</li><li>x4</li><li>x5</li><li>x6</li>
    </ul>
    <ul class="list" style="left:139px;top:181px;">
      <li>12-5AM</li>
      <li>5AM-10AM</li>
      <li>10AM-2PM</li>
      <li>2PM-5PM</li>
      <li>5PM-8PM</li>
      <li>8PM-12PM</li>
    </ul>
  </section>

  <section class="screen row-2 col-3">
    <div class="screen-brand">Brindle</div>
    <div class="screen-user screen-user--light">Sarah</div>
    <div class="label" style="left:7px;top:162px;">Trigger</div>
    <ul class="list" style="left:9px;top:183px;line-height:16.8px;">
      <li>Week</li>
      <li>Month</li>
      <li>Quarter (3 months)</li>
      <li>Semi (6 months)</li>
      <li>Year</li>
    </ul>
  </section>

</body>
</html>
```